Harbourline Service Allies Wordpress Design

See attached brief. If you have questions beyond this please let me know. Brief document is HS Allies Website Design v1. Other documents are files from logo creation and business cards to give you an idea of colours and images. Also see document that shows examples of the types of images I want to display on the website.

Focus of site is for customers and to drive traffic from social media etc. Company is startup consulting business in Customer Experience and Contact Centre. We offer benchmarking, strategy reviews, technology audits. etc

Looking for the site to use the existing Wordpress theme on hostNest or something compatible. Happy to change if there is a good reason for doing so.

Has to be easy to manage ongoing if possible.

Target Market(s)

HSA is a consulting organisation in contact centre and customer experience

Number of Pages Required

4 page

Font styles to use
Serif
Sans Serif

Colors
0255a3
3276b5
33a6d7
0293ce
ffffff
fefdec

Requirements
Must have
• Hosted on hostNest so must be compatible. Preference is to use the theme that is already there (Lumeo) unless there is a reason not to
Nice to have
• see brief

```html
<!DOCTYPE html>
<html lang="en">
<head>
<meta charset="utf-8">
<title>Harbourline Service Allies</title>
<link href="https://fonts.googleapis.com/css2?family=Open+Sans:wght@300;400;600&family=Roboto:wght@300;400;500&display=swap" rel="stylesheet">
<style>
:root{
  --page:#ffffff;
  --ink:#333333;
  --muted:#8a8a8a;
  --accent:#1ea3e6;
  --brand:#0255a3;
  --red:#e0444f;
  --green:#7cb13b;
  --green-ring:#dcefc8;
  --ring:#ececec;
  --footer:#262626;
  --footer-deep:#1f1f1f;
  --footer-line:#4a4a4a;
  --footer-text:#c9c9c9;
  --footer-dim:#7a7a7a;
  --tag:#3a3a3a;
  --field:#2e2e2e;
}
*{box-sizing:border-box;margin:0;padding:0}
html,body{width:776px;height:1200px;overflow:hidden;background:var(--page)}
body{position:relative;font-family:"Roboto",sans-serif;color:var(--ink)}
.abs{position:absolute}

/* header */
.brand{left:32px;top:10px;width:190px;text-align:center;color:var(--brand);font-family:"Open Sans",sans-serif;font-weight:600}
.brand-mark{display:flex;align-items:center;justify-content:center;gap:6px;font-size:30px;line-height:34px;letter-spacing:2px}
.brand-mark i{display:block;width:14px;height:14px;border-radius:50%;background:var(--accent)}
.brand-name{font-size:12.5px;line-height:16px;letter-spacing:.3px;border-top:1px solid var(--brand);margin-top:6px;padding-top:4px}
.nav-item{top:45px;font-family:"Open Sans",sans-serif;font-size:11px;line-height:14px;color:#444;white-space:nowrap;text-decoration:none}
.nav-underline{left:417px;top:72px;width:46px;height:3px;background:var(--accent)}
.search{left:727px;top:40px;width:24px;height:24px;border-radius:50%;background:#eee;display:flex;align-items:center;justify-content:center}

/* hero */
.hero{left:22px;top:73px;width:735px;height:285px;overflow:hidden;
  background:linear-gradient(100deg,#b9bec2 0%,#dfe2e4 30%,#eef0f1 48%,#8f8377 62%,#5f5a56 75%,#2f2f31 100%)}
.hero-slogan{left:0;width:100%;top:106px;text-align:center;font-family:"Open Sans",sans-serif;font-size:29px;color:#fff;letter-spacing:-.3px}
.hero-slogan span{color:var(--accent)}
.hero-sub{left:0;width:100%;top:141px;text-align:center;font-family:"Open Sans",sans-serif;font-weight:300;font-size:19px;color:#fff;letter-spacing:1px}

/* intro */
.intro-title{left:0;width:776px;top:378px;text-align:center;font-family:"Open Sans",sans-serif;font-size:24px;font-weight:400;color:#333}
.intro-rule{left:154px;top:420px;width:474px;height:1px;background:#e4e4e4}
.intro-text{left:0;width:776px;top:423px;text-align:center;font-weight:300;font-size:14.5px;line-height:20px;color:#777}

/* services */
.service{width:190px;text-align:center}
.service-ring{width:128px;height:128px;border-radius:50%;background:var(--ring);margin:0 auto;display:flex;align-items:center;justify-content:center}
.service-dot{width:108px;height:108px;border-radius:50%;background:var(--red);display:flex;align-items:center;justify-content:center}
.service.active .service-ring{background:var(--green-ring)}
.service.active .service-dot{background:var(--green)}
.service-title{margin-top:20px;font-family:"Open Sans",sans-serif;font-size:14px;font-weight:400;line-height:17px;color:#777}
.service.active .service-title{color:var(--green)}
.service-text{margin:7px auto 0;width:146px;font-size:9.6px;line-height:16.4px;color:var(--muted)}

/* footer */
.footer{left:17px;top:777px;width:742px;height:423px;background:var(--footer)}
.footer-bar{left:17px;top:1150px;width:742px;height:50px;background:var(--footer-deep)}
.col-head{font-size:13px;font-weight:400;color:var(--footer-text);padding-bottom:5px;border-bottom:1px solid var(--footer-line)}
.news{left:24px;top:810px;width:232px}
.news-item{display:flex;gap:8px;height:52px}
.news-list{margin-top:24px}
.thumb{width:53px;height:43px;flex:none;border:2px solid #ddd}
.news-cat{font-size:7px;color:var(--footer-text);line-height:9px;margin-top:1px}
.news-title{font-size:10.8px;color:#fff;line-height:14px;margin-top:2px;font-weight:500;white-space:nowrap}
.news-title.hot{color:var(--accent)}
.news-meta{font-size:7px;color:var(--footer-text);line-height:10px}
.news-meta b{font-size:8px;color:#fff}
.tags{left:270px;top:810px;width:233px}
.tag-cloud{display:flex;flex-wrap:wrap;gap:7px 6px;margin-top:21px;width:240px}
.tag{font-size:7.8px;letter-spacing:.1px;color:var(--footer-text);background:var(--tag);height:17px;line-height:17px;padding:0 8px;white-space:nowrap}
.tag.on{background:var(--accent);color:#fff}
.partners{left:270px;top:987px;width:233px}
.partner-list{list-style:none;margin-top:14px}
.partner-list li{font-size:8px;line-height:14.5px;color:var(--footer-dim);padding-left:12px;position:relative}
.partner-list li::before{content:"";position:absolute;left:1px;top:5px;width:4px;height:4px;border-right:1px solid currentColor;border-bottom:1px solid currentColor;transform:rotate(-45deg)}
.partner-list li.on{color:#fff;padding-left:16px}
.contact{left:521px;top:810px;width:231px}
.contact-lines{margin-top:20px;font-size:9px;line-height:14.5px;color:var(--footer-text)}
.contact-lines div{display:flex;align-items:center;gap:6px}
.contact-lines svg{flex:none}
.field{width:231px;background:var(--field);border:1px solid #333;font-size:8px;color:#777;padding:4px 3px;margin-top:7px}
.field.short{height:22px}
.field.area{height:99px}
.send{left:663px;top:1077px;width:82px;height:19px;border-radius:10px;background:#1b1b1b;color:#fff;font-size:8.5px;line-height:19px;text-align:center}
.social{left:581px;top:1167px;display:flex;gap:9px;align-items:center}
.social span{display:block;width:14px;height:14px;border-radius:3px;background:#e8e8e8}
.social span.first{width:25px;height:25px;border-radius:2px;background:#3b5ea8;margin-right:2px}
</style>
</head>
<body>

<header>
  <div class="abs brand">
    <div class="brand-mark"><i></i>HSA</div>
    <div class="brand-name">Harbourline Service Allies</div>
  </div>
  <nav>
    <a class="abs nav-item" style="left:427px">Home</a>
    <a class="abs nav-item" style="left:480px">Services</a>
    <a class="abs nav-item" style="left:542px">Partners</a>
    <a class="abs nav-item" style="left:604px">Blog</a>
    <a class="abs nav-item" style="left:651px">Touch with Us</a>
    <div class="abs nav-underline"></div>
  </nav>
  <div class="abs search">
    <svg width="10" height="10" viewBox="0 0 10 10"><circle cx="4" cy="4" r="3" fill="none" stroke="#999" stroke-width="1.2"/><line x1="6.2" y1="6.2" x2="9" y2="9" stroke="#999" stroke-width="1.4"/></svg>
  </div>
</header>

<section class="abs hero" role="img" aria-label="Photo of a consultant with a headset reading a tablet in a bright office">
  <svg class="abs" style="left:10px;top:115px" width="22" height="50" viewBox="0 0 22 50"><polyline points="20,2 2,25 20,48" fill="none" stroke="#fff" stroke-width="1.2"/></svg>
  <svg class="abs" style="left:703px;top:115px" width="22" height="50" viewBox="0 0 22 50"><polyline points="2,2 20,25 2,48" fill="none" stroke="#fff" stroke-width="1.2" opacity=".7"/></svg>
  <div class="abs hero-slogan"><span>SHOW</span> YOUR REMARKABLE SLOGAN</div>
  <div class="abs hero-sub">Put your Images, Videos here</div>
</section>

<section>
  <h1 class="abs intro-title">Harbourline Service Allies (HS Allies)</h1>
  <div class="abs intro-rule"></div>
  <p class="abs intro-text">is a consulting company focused on Customer Experience<br>and Contact Centre Solutions.</p>
</section>

<section>
  <div class="abs service" style="left:8px;top:494px">
    <div class="service-ring"><div class="service-dot">
      <svg width="44" height="38" viewBox="0 0 44 38"><rect x="3" y="3" width="38" height="24" fill="none" stroke="#fff" stroke-width="3"/><rect x="16" y="29" width="12" height="4" fill="#fff"/><rect x="10" y="33" width="24" height="3" fill="#fff"/></svg>
    </div></div>
    <h3 class="service-title">Contact Centre<br>Benchmarketing</h3>
    <p class="service-text">High resolution graphics and responsive layout makes theme look great and crisp on any device and screen size.</p>
  </div>
  <div class="abs service active" style="left:199px;top:494px">
    <div class="service-ring"><div class="service-dot">
      <svg width="30" height="44" viewBox="0 0 30 44"><path d="M15 3a12 12 0 0 0-7 21.7c1.4 1.1 2 2.6 2 4.3v2h10v-2c0-1.7.6-3.2 2-4.3A12 12 0 0 0 15 3z" fill="none" stroke="#fff" stroke-width="2.6"/><line x1="10" y1="35" x2="20" y2="35" stroke="#fff" stroke-width="2.6"/><line x1="11.5" y1="40" x2="18.5" y2="40" stroke="#fff" stroke-width="2.6"/></svg>
    </div></div>
    <h3 class="service-title">Understand Why your<br>customers are calling</h3>
    <p class="service-text">High resolution graphics and responsive layout makes theme look great and crisp on any device and screen size.</p>
  </div>
  <div class="abs service" style="left:390px;top:494px">
    <div class="service-ring"><div class="service-dot">
      <svg width="40" height="42" viewBox="0 0 40 42"><path d="M13 4a3 3 0 0 1 6 0v14l12 2c3 .6 4 2.5 4 5v7c0 4-3 6-6 6H18c-2 0-3-1-4-2L5 25c-1.5-1.5 0-4 2.5-3.2L13 25z" fill="#fff"/><rect x="14" y="37" width="20" height="4" fill="#fff"/></svg>
    </div></div>
    <h3 class="service-title">Benchmark your<br>outsourcing Partners</h3>
    <p class="service-text" style="margin-top:3px">High resolution graphics and responsive layout makes theme look great and crisp on any device and screen size.</p>
  </div>
  <div class="abs service" style="left:580px;top:494px">
    <div class="service-ring"><div class="service-dot">
      <svg width="46" height="34" viewBox="0 0 46 34"><rect x="8" y="3" width="30" height="22" fill="none" stroke="#fff" stroke-width="3"/><path d="M2 27h42l-3 5H5z" fill="#fff"/></svg>
    </div></div>
    <h3 class="service-title">Cloud Readiness<br>Assessment</h3>
    <p class="service-text">High resolution graphics and responsive layout makes theme look great and crisp on any device and screen size.</p>
  </div>
</section>

<footer>
  <div class="abs footer"></div>
  <div class="abs footer-bar"></div>

  <div class="abs news">
    <h4 class="col-head">Latest News</h4>
    <div class="news-list">
      <div class="news-item">
        <div class="thumb" role="img" aria-label="Photo of colleagues at a laptop" style="background:linear-gradient(135deg,#9fb3c4,#e3e6e8,#6b7b88)"></div>
        <div><div class="news-cat">News</div><div class="news-title">Job Seeking Out of Your Industry</div><div class="news-meta">12 Dec 2012 / <b>by</b> Dana Ellery</div></div>
      </div>
      <div class="news-item">
        <div class="thumb" role="img" aria-label="Photo of a group of smiling children" style="background:linear-gradient(135deg,#3aa15a,#e0b24a,#c8433c)"></div>
        <div><div class="news-cat">News</div><div class="news-title hot">Magnifying Uses of Small Spaces</div><div class="news-meta">12 Dec 2012 / <b>by</b> Dana Ellery</div></div>
      </div>
      <div class="news-item">
        <div class="thumb" role="img" aria-label="Photo of a graduate in glasses" style="background:linear-gradient(135deg,#d8cbb5,#f2ede4,#7b6a55)"></div>
        <div><div class="news-cat">News</div><div class="news-title">What Your College Degree Will Be</div><div class="news-meta">12 Dec 2012 / <b>by</b> Dana Ellery</div></div>
      </div>
      <div class="news-item">
        <div class="thumb" role="img" aria-label="Photo of a city street at night" style="background:linear-gradient(135deg,#1f4c5c,#4f8a7a,#c2506a)"></div>
        <div><div class="news-cat">News</div><div class="news-title">The Street Aesthetic of New York</div><div class="news-meta">12 Dec 2012 / <b>by</b> Dana Ellery</div></div>
      </div>
      <div class="news-item">
        <div class="thumb" role="img" aria-label="Photo of a photographer outdoors" style="background:linear-gradient(135deg,#e9eef2,#9fb4c6,#5d6d7a)"></div>
        <div><div class="news-cat">News</div><div class="news-title">How to do Levitation Photography</div><div class="news-meta">12 Dec 2012 / <b>by</b> Dana Ellery</div></div>
      </div>
    </div>
  </div>

  <div class="abs tags">
    <h4 class="col-head">Tags</h4>
    <div class="tag-cloud">
      <span class="tag">FEATURES</span><span class="tag">INSPIRATION</span><span class="tag">SHOWCASE</span>
      <span class="tag">GRAPHIC DESIGN</span><span class="tag on">ILLUSTRATION</span><span class="tag">DESIGN</span>
      <span class="tag">WEB DESIGN</span><span class="tag">VIDEO</span><span class="tag">ART</span><span class="tag">NEW WORK</span>
      <span class="tag">ANIMATION</span><span class="tag">PHOTOSHOP</span><span class="tag">DIGITAL PAINTING</span>
      <span class="tag">CG</span><span class="tag">HOWTO</span>
    </div>
  </div>

  <div class="abs partners">
    <h4 class="col-head">Partner Websites</h4>
    <ul class="partner-list">
      <li>Tessel Build Services</li>
      <li class="on">Brightfield Power Group</li>
      <li>Pinegate Web Studio</li>
      <li>Fernway Trade Association</li>
      <li>Lumen Lane Photography</li>
    </ul>
  </div>

  <div class="abs contact">
    <h4 class="col-head">Contact info</h4>
    <div class="contact-lines">
      <div><svg width="9" height="9" viewBox="0 0 9 9"><path d="M1 4.5 4.5 1 8 4.5V8H1z" fill="#555"/></svg>48 Quayside Row, Portmere, PM 20417</div>
      <div><svg width="9" height="9" viewBox="0 0 9 9"><rect x="1" y="2" width="7" height="5" rx="1" fill="#555"/></svg>+1 555 0142</div>
      <div><svg width="9" height="9" viewBox="0 0 9 9"><rect x="0.5" y="2" width="8" height="5.5" fill="#555"/><polyline points="0.5,2 4.5,5 8.5,2" fill="none" stroke="#777" stroke-width=".8"/></svg>hello@hsallies.example</div>
    </div>
    <div class="field short" style="margin-top:12px">Your name ...</div>
    <div class="field short">E-mail ...</div>
    <div class="field area">Your message ...</div>
  </div>
  <div class="abs send">SEND MESSAGE</div>

  <div class="abs social" aria-label="Social links">
    <span class="first"></span><span></span><span></span><span></span><span></span><span></span><span></span>
  </div>
</footer>

</body>
</html>
```